Outpatient Mental Health Clinic needs a good brochure

We are an outpatient clinic in Michigan, USA and provide therapy and evaluation services for adults, adolescents, and children. Our psychologists, social workers, and counselors help individuals who present with a host of psychological difficulties. Our goal for the brochure is to give an overview of our services so that our marketing person can pass them out to physicians and other referral sources.

Target Market(s)

Our target market are patients who are seeking referrals through their primary care physicians.

Industry/Entity Type

Clinic

Font styles to use
Serif
Sans Serif

Colors
fbf289
f68d4c
f37122
ffffff

Requirements
Must have
• My project must be illustrative enough to show what services are provided. Pictures of individuals is also important.
Nice to have
• In addition to content I would like to have pictures of individuals.

```html
<!DOCTYPE html>
<html lang="en">
<head>
<meta charset="utf-8">
<title>Lakeshore Counseling — Inside Spread</title>
<link rel="stylesheet" href="https://fonts.googleapis.com/css2?family=Open+Sans:wght@400;600&display=swap">
<style>
  :root {
    --page-bg: #d9d9d9;
    --paper: #ffffff;
    --brand-orange: #f37122;
    --brand-coral: #f68d4c;
    --brand-yellow: #fbf289;
    --body-grey: #5b5b5b;
    --photo-clinic-a: #d8c2ae;
    --photo-clinic-b: #a9b3c2;
    --map-a: #efe9d8;
    --map-b: #e2dcc6;
    --photo-family-a: #f3e1d6;
    --photo-family-b: #dcb8a0;
    --divider-shadow: rgba(0,0,0,0.12);
  }
  * { box-sizing: border-box; margin: 0; padding: 0; }
  html, body {
    width: 1200px; height: 800px; overflow: hidden;
    background: var(--page-bg);
    font-family: "Open Sans", Arial, sans-serif;
  }
  .spread {
    position: absolute; left: 60px; top: 80px;
    width: 1080px; height: 640px;
    background: var(--paper);
    box-shadow: 0 12px 30px rgba(0,0,0,0.18);
    overflow: hidden;
  }
  .panel { position: absolute; top: 0; width: 360px; height: 640px; }
  .panel--left { left: 0; }
  .panel--middle { left: 360px; }
  .panel--right { left: 720px; }
  .fold-line {
    position: absolute; top: 0; width: 1px; height: 640px;
    background: rgba(0,0,0,0.06); z-index: 5;
  }

  .section-title {
    position: absolute; left: 30px;
    width: 250px; padding: 6px 14px 8px;
    border: 2px solid var(--brand-orange);
    border-bottom-width: 6px;
    font-size: 27px; line-height: 1.0; font-weight: 400;
    color: var(--brand-orange);
  }
  .section-title--on-band { border-color: var(--paper); color: var(--paper); }
  .body-copy {
    position: absolute; left: 30px; width: 290px;
    font-size: 15px; line-height: 1.2; text-align: justify;
    color: var(--body-grey);
  }
  .body-copy--on-band { color: var(--paper); }

  .photo { position: absolute; }
  .photo--clinic {
    left: 0; top: 0; width: 360px; height: 400px;
    background: linear-gradient(100deg, var(--photo-clinic-a) 0%, #efe7dd 45%, var(--photo-clinic-b) 100%);
  }
  .photo--family {
    left: 0; top: 380px; width: 360px; height: 260px;
    background: linear-gradient(160deg, var(--photo-family-a) 0%, var(--photo-family-b) 100%);
  }
  .map {
    position: absolute; left: 0; top: 150px; width: 360px; height: 250px;
    background: linear-gradient(150deg, var(--map-a) 0%, var(--map-b) 100%);
  }

  .color-band { position: absolute; left: 0; top: 0; z-index: 2; }
  .right-curves { position: absolute; left: 720px; top: 0; z-index: 2; }

  .service-list {
    position: absolute; left: 400px; top: 410px; width: 300px;
    list-style: none; z-index: 3;
  }
  .service-list li {
    position: relative; padding-left: 24px; margin-bottom: 14px;
    font-size: 15px; line-height: 1.2; color: var(--paper);
  }
  .service-list li::before {
    content: ""; position: absolute; left: 0; top: 5px;
    width: 10px; height: 10px; border-radius: 50%; background: var(--brand-yellow);
  }

  .pull-quote {
    position: absolute; left: 760px; top: 26px; width: 290px;
    font-size: 16px; line-height: 1.3; text-align: center;
    color: var(--brand-coral); z-index: 3;
  }
  .brand-tag {
    position: absolute; left: 790px; top: 150px;
    width: 190px; padding: 10px 14px;
    background: var(--brand-orange); border: 3px solid var(--paper);
    border-radius: 10px; color: var(--paper);
    z-index: 4;
  }
  .brand-tag__name { font-size: 17px; line-height: 1.15; font-weight: 600; }
  .brand-tag__line { font-size: 10px; line-height: 1.4; font-weight: 600; margin-top: 2px; }
</style>
</head>
<body>
  <main class="spread">
    <section class="panel panel--left">
      <h2 class="section-title" style="top:22px;">About Our<br>Clinic</h2>
      <p class="body-copy" style="top:116px;">We are an outpatient mental health clinic in Michigan offering therapy and evaluation for adults, adolescents and children. Our psychologists, social workers and counselors help people facing a wide range of psychological difficulties, from anxiety and depression to family stress. We work closely with primary care physicians so every referral receives prompt, caring attention.</p>
    </section>

    <section class="panel panel--middle">
      <div class="photo photo--clinic" role="img" aria-label="Photo: smiling clinician talking warmly with an older patient"></div>
    </section>

    <section class="panel panel--right">
      <div class="map" role="img" aria-label="Street map showing the clinic location"></div>
      <div class="photo photo--family" role="img" aria-label="Photo: happy family of parents and two young children lying together"></div>
    </section>

    <svg class="color-band" width="720" height="640" viewBox="0 0 720 640" aria-hidden="true">
      <path d="M0 352 C 180 338, 300 372, 360 386 C 470 404, 600 376, 720 332 L720 640 L0 640 Z" fill="var(--divider-shadow)" transform="translate(0,-6)"/>
      <path d="M0 352 C 180 338, 300 372, 360 386 C 470 404, 600 376, 720 332 L720 640 L0 640 Z" fill="var(--paper)" transform="translate(0,-3)"/>
      <path d="M0 352 C 180 338, 300 372, 360 386 C 470 404, 600 376, 720 332 L720 640 L0 640 Z" fill="var(--brand-orange)"/>
    </svg>

    <svg class="right-curves" width="360" height="640" viewBox="0 0 360 640" aria-hidden="true">
      <path d="M0 0 L360 0 L360 150 C 240 165, 110 185, 0 250 Z" fill="var(--paper)"/>
      <path d="M0 332 C 120 345, 240 360, 360 390 L360 400 C 240 372, 120 358, 0 345 Z" fill="var(--paper)"/>
    </svg>

    <div class="panel panel--left" style="z-index:3;">
      <h2 class="section-title section-title--on-band" style="top:400px;">Our<br>Services</h2>
      <p class="body-copy body-copy--on-band" style="top:494px;">Every new patient begins with a careful intake and evaluation. Our team then builds a plan that fits the person, whether weekly therapy, family sessions or psychological testing. Evening hours fit school and work schedules.</p>
    </div>

    <ul class="service-list">
      <li>Individual therapy for adults and adolescents</li>
      <li>Child and family counseling sessions</li>
      <li>Psychological testing and evaluation</li>
      <li>Care for anxiety, depression and trauma</li>
      <li>Fast referral intake for physicians</li>
    </ul>

    <blockquote class="pull-quote">“Caring, evidence-based mental health support for adults, adolescents and children, close to home.”</blockquote>

    <div class="brand-tag">
      <div class="brand-tag__name">Lakeshore Counseling</div>
      <div class="brand-tag__line">Outpatient Mental Health Clinic</div>
    </div>

    <div class="fold-line" style="left:360px;"></div>
    <div class="fold-line" style="left:720px;"></div>
  </main>
</body>
</html>
```